Bakery looking for new Business cards

I have a new logo and now its time to upgrade our business cards.
e-mail - info@corvelbakehouse.com
www.corvelbakehouse.com
847-619-2837

518w Pellow Brook rd. Bloomingdale IL 60473
Bakery Hour's Wednesday-Sunday 7AM-4PM

Industry/Entity Type

Bakery

Contact Information for Business Card

Hr's

Requirements
Must have
• Business information.
Nice to have
• would like to include a QR code for our website.

```html
<!DOCTYPE html>
<html lang="en">
<head>
<meta charset="utf-8">
<title>Corvel's bakery — Business Card</title>
<link rel="stylesheet" href="https://fonts.googleapis.com/css2?family=Mulish:wght@400;600;700&family=Lobster&display=swap">
<style>
  :root {
    --gold: #e9b454;
    --gold-deep: #b9851f;
    --ink: #1b1712;
    --paper: #ffffff;
    --backdrop: #efe9df;
  }
  * { box-sizing: border-box; margin: 0; padding: 0; }
  html, body { width: 1200px; height: 780px; overflow: hidden; }
  body {
    background: var(--backdrop);
    font-family: "Mulish", sans-serif;
    color: var(--ink);
    position: relative;
  }
  .card {
    position: absolute;
    top: 234px;
    width: 545px;
    height: 311px;
    background: var(--gold);
    box-shadow: 0 6px 18px rgba(60, 40, 10, 0.22);
    overflow: hidden;
  }
  .card--front { left: 35px; }
  .card--back { left: 620px; }

  .front-panel { position: absolute; inset: 0; }

  .brand {
    position: absolute;
    left: 0;
    top: 0;
    width: 235px;
    height: 311px;
    display: flex;
    flex-direction: column;
    align-items: center;
    justify-content: center;
    gap: 8px;
  }
  .brand-mark {
    width: 34px;
    height: 34px;
    border-radius: 50%;
    background: var(--ink);
  }
  .brand-name {
    font-size: 25px;
    font-weight: 600;
    color: var(--ink);
    white-space: nowrap;
  }
  .brand-tagline {
    font-size: 13px;
    letter-spacing: 1px;
    color: var(--gold);
    font-weight: 600;
  }

  .contact {
    position: absolute;
    left: 300px;
    top: 44px;
    right: 20px;
  }
  .person-name {
    font-family: "Lobster", cursive;
    font-weight: 400;
    font-size: 33px;
    line-height: 1;
    color: var(--ink);
  }
  .person-role {
    font-size: 15px;
    margin-top: 4px;
    margin-bottom: 18px;
  }
  .contact-list { list-style: none; }
  .contact-item {
    display: flex;
    align-items: flex-start;
    gap: 9px;
    font-size: 13.5px;
    line-height: 1.3;
    margin-bottom: 6px;
    white-space: nowrap;
  }
  .contact-icon {
    flex: 0 0 15px;
    width: 15px;
    height: 15px;
    margin-top: 1px;
  }

  .back-pattern { position: absolute; inset: 0; background: var(--gold); }
  .back-brand {
    position: absolute;
    left: 0; right: 0; top: 100px;
    display: flex;
    align-items: center;
    justify-content: center;
    gap: 14px;
  }
  .back-brand .brand-mark { width: 44px; height: 44px; }
  .back-brand .brand-name { font-size: 38px; }
  .hours {
    position: absolute;
    left: 0; right: 0; bottom: 26px;
    text-align: center;
    font-size: 13px;
    letter-spacing: 1.2px;
    text-transform: uppercase;
    white-space: nowrap;
  }
</style>
</head>
<body>

  <section class="card card--front">
    <svg class="front-panel" width="545" height="311" viewBox="0 0 545 311">
      <path d="M0 0 H222 Q262 40 258 120 Q255 145 232 155 Q255 165 258 190 Q262 270 222 311 H0 Z"
            fill="var(--paper)" stroke="var(--gold-deep)" stroke-width="2"/>
    </svg>

    <div class="brand">
      <span class="brand-mark"></span>
      <span class="brand-name">Corvel's bakery</span>
      <span class="brand-tagline">DESSERT SHOP</span>
    </div>

    <div class="contact">
      <h1 class="person-name">Daniel Brooks</h1>
      <p class="person-role">Founder &amp; CEO</p>
      <ul class="contact-list">
        <li class="contact-item">
          <svg class="contact-icon" viewBox="0 0 16 16"><circle cx="8" cy="8" r="8" fill="var(--ink)"/><path d="M8 3.5a2.8 2.8 0 0 0-2.8 2.8C5.2 8.5 8 12 8 12s2.8-3.5 2.8-5.7A2.8 2.8 0 0 0 8 3.5z" fill="var(--gold)"/><circle cx="8" cy="6.3" r="1" fill="var(--ink)"/></svg>
          <span>518w Pellow Brook rd.<br>Ashford Park, IL 60473</span>
        </li>
        <li class="contact-item">
          <svg class="contact-icon" viewBox="0 0 16 16"><circle cx="8" cy="8" r="8" fill="var(--ink)"/><path d="M5.2 4h1.6l.8 2-1 .8a5 5 0 0 0 2.6 2.6l.8-1 2 .8v1.6c0 .5-.4.9-.9.9A6.8 6.8 0 0 1 4.3 4.9c0-.5.4-.9.9-.9z" fill="var(--gold)"/></svg>
          <span>847-619-2837</span>
        </li>
        <li class="contact-item">
          <svg class="contact-icon" viewBox="0 0 16 16"><circle cx="8" cy="8" r="8" fill="var(--ink)"/><rect x="4" y="5" width="8" height="6" rx="0.8" fill="var(--gold)"/><path d="M4.3 5.4 8 8.3l3.7-2.9" fill="none" stroke="var(--ink)" stroke-width="0.9"/></svg>
          <span>info@corvelbakehouse.com</span>
        </li>
        <li class="contact-item">
          <svg class="contact-icon" viewBox="0 0 16 16"><circle cx="8" cy="8" r="8" fill="var(--ink)"/><circle cx="8" cy="8" r="4" fill="none" stroke="var(--gold)" stroke-width="1"/><path d="M4 8h8M8 4c-1.6 2.2-1.6 5.8 0 8M8 4c1.6 2.2 1.6 5.8 0 8" fill="none" stroke="var(--gold)" stroke-width="0.8"/></svg>
          <span>corvelbakehouse.com</span>
        </li>
      </ul>
    </div>
  </section>

  <section class="card card--back">
    <div class="back-pattern" role="img" aria-label="Subtle diamond lattice pattern with small dots and repeated bakery motifs in a slightly darker gold"></div>
    <div class="back-brand">
      <span class="brand-mark"></span>
      <span class="brand-name">Corvel's bakery</span>
    </div>
    <p class="hours">Bakery Hour's Wednesday-Sunday 7am-4pm</p>
  </section>

</body>
</html>
```